Estate Agent/NORTHGATE HOMES valuation tool

We need a design for our our new estate agent valuation tool.

The tool allows users to book a valuation of their house/property with the estate agent, after they choose there property they can then complete their details and choose a booking time.

The mock up of the design we want is attached to this project.(Main Screen)

This also needs to be responsive so the design is easy to use on a mobile device.

Target Market(s)

estate agents

Industry/Entity Type

NORTHGATE HOMES Agent

Number of Pages Required

1 page

Requirements
Must have
• Section 2 and 3 greyed out when user is on step 1
• Section 1 and 3 greyed out when user is on step 2
• Section 1 and 2 greyed out when the user is on step 3
• *** Design must be shown for mobile/ipad and desktop
Nice to have
• Clean and Simple
Should not have
• Dark colours

```html
<!DOCTYPE html>
<html lang="en">
<head>
<meta charset="utf-8">
<title>Book Your Valuation Online – Design Sheet</title>
<link rel="stylesheet" href="https://fonts.googleapis.com/css2?family=Oswald:wght@500&family=Source+Sans+3:ital,wght@0,400;0,600;0,700;1,400&display=swap">
<style>
:root{
  --sheet:#efefef;
  --green:#a4c93a;
  --blue:#2592d6;
  --orange:#f08a2b;
  --navy:#0c4673;
  --city-top:#2a3f5c;
  --city-bottom:#1a2b44;
  --card-head:#ffffff;
  --card-body:#f0f0f0;
  --muted-body:#dadada;
  --muted-btn:#b3b3b3;
  --muted-step:#c9c9c9;
  --label:#6b6b6b;
  --field-border:#dcdcdc;
  --placeholder:#b9b9b9;
  --alert:#d9161c;
  --caption-blue:#1e6fc4;
  --caption-green:#9fb422;
}
*{box-sizing:border-box;margin:0;padding:0}
html,body{width:881px;height:1200px;overflow:hidden;background:var(--sheet)}
body{font-family:"Source Sans 3",Arial,sans-serif}
.stage{width:954px;height:1300px;position:relative;transform:scale(0.92348);transform-origin:0 0}

.mockup{position:absolute;width:850px;height:530px;overflow:hidden;box-shadow:0 1px 3px rgba(0,0,0,.25)}
.mockup--static{left:53px;top:41px}
.mockup--live{left:56px;top:681px}
.city-backdrop{position:absolute;inset:0;background:linear-gradient(180deg,var(--city-top) 0%,#30486a 45%,var(--city-bottom) 100%)}

.brand{position:absolute;left:0;right:0;top:68px;text-align:center;color:#fff}
.brand__mark{display:inline-block;width:14px;height:14px;background:#fff;margin-bottom:6px}
.brand__name{font-weight:700;font-size:19px;letter-spacing:.5px;line-height:1}
.brand__slogan{font-size:9px;margin-top:2px}

.headline{position:absolute;left:0;right:0;top:116px;text-align:center;color:#fff;font-weight:700;font-size:16px;letter-spacing:.3px}

.progress{position:absolute;left:193px;top:147px;width:458px;height:32px}
.progress__track{position:absolute;top:15px;height:3px}
.progress__step{position:absolute;top:0;width:32px;height:32px;border-radius:50%;border:2px solid #fff;color:#fff;font-weight:700;font-size:15px;display:flex;align-items:center;justify-content:center}

.card{position:absolute;top:192px;width:199px;height:249px;background:var(--card-body);box-shadow:0 1px 2px rgba(0,0,0,.3)}
.card--property{left:114px}.card--details{left:326px}.card--time{left:538px}
.card__head{height:38px;background:var(--card-head);border-bottom:1px solid #e2e2e2;display:flex;align-items:center;justify-content:space-between;padding:0 13px;color:var(--label);font-size:10.5px}
.card__head svg{width:20px;height:20px;fill:#bdbdbd}
.card__button{position:absolute;left:0;right:0;bottom:0;height:25px;color:#fff;font-weight:600;font-size:11px;display:flex;align-items:center;justify-content:center}
.card--property .card__button{background:var(--green)}
.card--details .card__button{background:var(--blue)}
.card--time .card__button{background:var(--orange)}

.field{position:absolute;left:14px;width:169px;height:18px;background:#fff;border:1px solid var(--field-border);font-size:6.5px;font-style:italic;color:var(--placeholder);padding-left:5px;display:flex;align-items:center}
.field--postcode{width:120px}
.search-button{position:absolute;left:134px;top:54px;width:50px;height:18px;background:var(--green);color:#fff;font-size:8px;display:flex;align-items:center;justify-content:center}

.day-tabs{position:absolute;left:13px;top:55px;display:flex;gap:2px}
.day-tab{width:22.3px;height:17px;background:#d6d6d6;color:#fff;font-size:4.5px;display:flex;align-items:center;justify-content:center}
.day-tab--active{background:var(--orange)}
.slot{position:absolute;left:13px;width:170px;height:18px;display:flex}
.slot__date{flex:1;background:#fff;border:1px solid var(--field-border);font-size:6.5px;font-style:italic;color:var(--placeholder);padding-left:5px;display:flex;align-items:center}
.slot__time{width:34px;background:var(--orange);color:#fff;font-size:8.5px;display:flex;align-items:center;justify-content:center}

.footer{position:absolute;left:0;right:0;bottom:0;height:39px;background:var(--navy);display:flex;justify-content:center;align-items:center;gap:21px;color:#fff;font-size:8.5px;font-weight:600}

/* greyed-out state for inactive steps */
.card--muted{background:var(--muted-body)}
.card--muted .card__head{background:#ebebeb}
.card--muted .card__button{background:var(--muted-btn)}
.card--muted .field,.card--muted .slot__date{background:#e6e6e6;border-color:#cfcfcf}
.card--muted .slot__time{background:#a9a9a9}
.card--muted .day-tab{background:#c5c5c5}
.field--locked{background:#f2f2f2;border-color:#e4e4e4;color:#cfcfcf}

.alert-tag{position:absolute;left:17px;top:38px;width:103px;height:12px;background:var(--alert);color:#fff;font-size:5.5px;font-weight:600;display:flex;align-items:center;padding-left:5px}
.alert-tag::after{content:"";position:absolute;left:3px;bottom:-4px;border-left:4px solid var(--alert);border-bottom:4px solid transparent}
.pointer{position:absolute;left:151px;top:65px;width:12px;height:14px}

.caption{position:absolute;left:0;right:0;text-align:center;font-family:"Oswald",Arial,sans-serif;font-weight:500;font-size:37px;line-height:1;letter-spacing:-.5px}
.caption--static{top:590px}
.caption--live{top:1228px}
.caption__blue{color:var(--caption-blue)}
.caption__green{color:var(--caption-green)}
</style>
</head>
<body>
<div class="stage">

  <!-- Step overview: all sections active -->
  <section class="mockup mockup--static">
    <div class="city-backdrop" role="img" aria-label="Aerial photograph of a dense city skyline with a blue tint"></div>
    <div class="brand"><div class="brand__name">NORTHGATE HOMES</div><div class="brand__slogan">Your text slogan here</div></div>
    <h1 class="headline">BOOK YOUR VALUATION ONLINE</h1>
    <div class="progress">
      <div class="progress__track" style="left:16px;width:140px;background:var(--green)"></div>
      <div class="progress__track" style="left:156px;width:160px;background:var(--blue)"></div>
      <div class="progress__track" style="left:316px;width:126px;background:var(--orange)"></div>
      <div class="progress__step" style="left:0;background:var(--green)">1</div>
      <div class="progress__step" style="left:213px;background:var(--blue)">2</div>
      <div class="progress__step" style="left:425px;background:var(--orange)">3</div>
    </div>

    <div class="card card--property">
      <div class="card__head">PROPERTY DETAILS<svg viewBox="0 0 20 20"><path d="M10 2 1 10h3v8h5v-5h2v5h5v-8h3z"/></svg></div>
      <div class="field field--postcode" style="top:54px">Post Code</div>
      <div class="search-button">Search</div>
      <div class="field" style="top:80px">123, Test Street</div>
      <div class="field" style="top:107px">Test City</div>
      <div class="field" style="top:133px">Test Country</div>
      <div class="card__button">PROCEED</div>
    </div>
    <div class="card card--details">
      <div class="card__head">YOUR DETAILS<svg viewBox="0 0 20 20"><circle cx="10" cy="6" r="4"/><path d="M3 19c0-5 3-8 7-8s7 3 7 8z"/></svg></div>
      <div class="field" style="top:54px">First Name</div>
      <div class="field" style="top:80px">Last Name</div>
      <div class="field" style="top:107px">Email Address</div>
      <div class="field" style="top:133px">Contact Number</div>
      <div class="card__button">PROCEED</div>
    </div>
    <div class="card card--time">
      <div class="card__head">APPOINTMENT TIME<svg viewBox="0 0 20 20"><path d="M2 4h14v6h-1.5V8H3.5v8H10v1.5H2z"/><circle cx="15" cy="15" r="4" fill="none" stroke="#bdbdbd" stroke-width="1.5"/><path d="M15 13v2h1.5" fill="none" stroke="#bdbdbd" stroke-width="1.2"/></svg></div>
      <div class="day-tabs"><div class="day-tab">Today</div><div class="day-tab day-tab--active">Mon 30th</div><div class="day-tab">Tue 1st</div><div class="day-tab">Wed 2nd</div><div class="day-tab">Thu 4th</div><div class="day-tab">Fri 5th</div><div class="day-tab">Sat 6th</div></div>
      <div class="slot" style="top:81px"><div class="slot__date">Monday 30th November</div><div class="slot__time">08:30</div></div>
      <div class="slot" style="top:107.5px"><div class="slot__date">Monday 30th November</div><div class="slot__time">10:30</div></div>
      <div class="slot" style="top:134px"><div class="slot__date">Monday 30th November</div><div class="slot__time">12:30</div></div>
      <div class="slot" style="top:160.5px"><div class="slot__date">Monday 30th November</div><div class="slot__time">14:30</div></div>
      <div class="slot" style="top:187px"><div class="slot__date">Monday 30th November</div><div class="slot__time">16:30</div></div>
      <div class="card__button">CONFIRM BOOKING</div>
    </div>

    <nav class="footer"><span>ABOUT US</span><span>BLOG</span><span>BUSSINESS</span><span>PRIVACY</span><span>CONTACT US</span></nav>
  </section>
  <div class="caption caption--static"><span class="caption__blue">STATIC</span> <span class="caption__green">DESIGN</span></div>

  <!-- Step one active, steps two and three greyed out -->
  <section class="mockup mockup--live">
    <div class="city-backdrop" role="img" aria-label="Aerial photograph of a dense city skyline with a blue tint"></div>
    <div class="brand"><div class="brand__name">NORTHGATE HOMES</div><div class="brand__slogan">Your text slogan here</div></div>
    <h1 class="headline">BOOK YOUR VALUATION ONLINE</h1>
    <div class="progress">
      <div class="progress__track" style="left:16px;width:140px;background:var(--green)"></div>
      <div class="progress__track" style="left:156px;width:286px;background:var(--muted-step)"></div>
      <div class="progress__step" style="left:0;background:var(--green)">1</div>
      <div class="progress__step" style="left:213px;background:var(--muted-step)">2</div>
      <div class="progress__step" style="left:425px;background:var(--muted-step)">3</div>
    </div>

    <div class="card card--property" style="background:#fff">
      <div class="card__head">PROPERTY DETAILS<svg viewBox="0 0 20 20"><path d="M10 2 1 10h3v8h5v-5h2v5h5v-8h3z"/></svg></div>
      <div class="field field--postcode" style="top:54px">Post Code</div>
      <div class="search-button">Search</div>
      <div class="alert-tag">Please Enter Your Post Code First</div>
      <svg class="pointer" viewBox="0 0 12 14"><path d="M3 1.5c.8 0 1.2.5 1.2 1.2V7l4.5.9c1 .2 1.5.8 1.4 1.8L9.6 13H4L1.3 8.6c-.4-.7.3-1.4 1-1l.6.5V2.7c0-.7.3-1.2 1-1.2z" fill="#fff" stroke="#333" stroke-width=".8"/></svg>
      <div class="field field--locked" style="top:80px">123, Test Street</div>
      <div class="field field--locked" style="top:107px">Test City</div>
      <div class="field field--locked" style="top:133px">Test Country</div>
      <div class="card__button">PROCEED</div>
    </div>
    <div class="card card--details card--muted">
      <div class="card__head">YOUR DETAILS<svg viewBox="0 0 20 20"><circle cx="10" cy="6" r="4"/><path d="M3 19c0-5 3-8 7-8s7 3 7 8z"/></svg></div>
      <div class="field" style="top:54px">First Name</div>
      <div class="field" style="top:80px">Last Name</div>
      <div class="field" style="top:107px">Email Address</div>
      <div class="field" style="top:133px">Contact Number</div>
      <div class="card__button">PROCEED</div>
    </div>
    <div class="card card--time card--muted">
      <div class="card__head">APPOINTMENT TIME<svg viewBox="0 0 20 20"><path d="M2 4h14v6h-1.5V8H3.5v8H10v1.5H2z"/><circle cx="15" cy="15" r="4" fill="none" stroke="#bdbdbd" stroke-width="1.5"/><path d="M15 13v2h1.5" fill="none" stroke="#bdbdbd" stroke-width="1.2"/></svg></div>
      <div class="day-tabs"><div class="day-tab">Today</div><div class="day-tab">Mon 30th</div><div class="day-tab">Tue 1st</div><div class="day-tab">Wed 2nd</div><div class="day-tab">Thu 4th</div><div class="day-tab">Fri 5th</div><div class="day-tab">Sat 6th</div></div>
      <div class="slot" style="top:81px"><div class="slot__date">Monday 30th November</div><div class="slot__time">08:30</div></div>
      <div class="slot" style="top:107.5px"><div class="slot__date">Monday 30th November</div><div class="slot__time">10:30</div></div>
      <div class="slot" style="top:134px"><div class="slot__date">Monday 30th November</div><div class="slot__time">12:30</div></div>
      <div class="slot" style="top:160.5px"><div class="slot__date">Monday 30th November</div><div class="slot__time">14:30</div></div>
      <div class="slot" style="top:187px"><div class="slot__date">Monday 30th November</div><div class="slot__time">16:30</div></div>
      <div class="card__button">CONFIRM BOOKING</div>
    </div>

    <nav class="footer"><span>ABOUT US</span><span>BLOG</span><span>BUSSINESS</span><span>PRIVACY</span><span>CONTACT US</span></nav>
  </section>
  <div class="caption caption--live"><span class="caption__blue">HOVER/ REAL</span> <span class="caption__green">DESIGN</span></div>

</div>
</body>
</html>
```